Marrowgate Gemworks Website revamp

Hi,

We need a working WordPress theme, not just a .PSD file. Thank you.

We need a complete revamp of our website. We sell lab grown diamonds online. We sell the idea that everyone should be able to afford a diamond. Thus our diamonds are priced very reasonably. Our selling point "the joy of giving and receiving a diamond in a little box".

Our range of products includes rings, bangles, necklace, ear rings etc. We currently only operate in Singapore. Some photos of our products are on our websites.

Need.
- Clean look and feel, simplistic preferably white and soft colours
- Easy to navigate
- No banners
- E Com
- Introduction page
- Willing to change logo if needed

Existing page: www.marrowgategemworks.com

Target Market(s)

Young ladies
Ladies
Men buying for ladies
Young boyfriends fresh out of school buying for love ones
Working ladies to match what they wear to work

Industry/Entity Type

Online

Requirements
Must have
• ECOM. Product shopping cart
Pictures uploads
Intro page
Nice to have
• Pastel colors preferred. - Color scheme is important in our business to create a long term impression. Color scheme will also be used for next potential project, i.e. packaging design.

Should not have
• Should not have old style fonts.

```html
<!DOCTYPE html>
<html lang="en">
<head>
<meta charset="utf-8">
<title>Marrowgate Gemworks</title>
<link href="https://fonts.googleapis.com/css2?family=Open+Sans:wght@400;600;700&family=Great+Vibes&display=swap" rel="stylesheet">
<style>
:root{
  --paper:#f3f1ee;
  --white:#ffffff;
  --ink:#3d3d3d;
  --muted:#666;
  --rule:#e2e2e2;
  --slate:#7a9099;
  --btn:#3b3b3b;
  --orange:#e58a1f;
  --green:#7fb13a;
  --red:#e0442f;
  --sky:#2aa5d3;
  --teal:#18a39a;
  --pink:#e8336d;
  --blue:#2a79b0;
  --price:#d9141c;
  --gold:#f5c95a;
}
*{box-sizing:border-box;margin:0;padding:0}
html,body{width:677px;height:1200px;overflow:hidden;background:var(--white)}
body{position:relative;font-family:"Open Sans",Arial,sans-serif;color:var(--ink)}
.abs{position:absolute}
a{color:inherit;text-decoration:none}

/* header */
.site-header{left:0;top:0;width:677px;height:98px;background:var(--paper)}
.brand{left:74px;top:22px;font-size:14px;font-weight:600;color:#6f6f6f;display:flex;align-items:center;gap:6px}
.brand-mark{width:10px;height:10px;border:1px solid #6f6f6f}
.account-links{right:74px;top:6px;font-size:7px;color:#555;text-align:right;line-height:11px}
.account-links .accent{color:#e88a9a}
.search{left:338px;top:36px;width:265px;height:19px;background:var(--white);font-size:6.5px;color:#999;padding:5px 6px}
.search svg{position:absolute;right:5px;top:4px}
.main-nav{left:74px;top:70px;width:403px;height:18px;border-top:1px solid #9aa9ae;border-bottom:1px solid #9aa9ae;font-size:7.5px;color:#444}
.main-nav span{position:absolute;top:3px}
.basket{left:477px;top:70px;width:126px;height:18px;background:var(--slate);color:#fff;font-size:6.5px;font-weight:600;display:flex;align-items:center;justify-content:center;gap:4px}

/* categories */
.category{width:122px;text-align:center}
.category .photo{width:122px;height:158px}
.cat-title{font-size:7px;font-weight:700;margin-top:9px;position:relative}
.cat-title:before,.cat-title:after{content:"";position:absolute;top:5px;width:34px;border-top:1px solid var(--rule)}
.cat-title:before{left:0}.cat-title:after{right:0}
.blurb{font-size:6.5px;line-height:10.5px;color:#555;margin-top:6px;padding:0 4px}
.btn{display:inline-block;background:var(--btn);color:#fff;font-size:6.5px;font-weight:600;width:56px;height:16px;line-height:16px;text-align:center}
.category .btn{margin-top:11px}

/* section heading */
.section-title{font-size:7px;font-weight:700;text-align:center}
.section-title span{background:var(--white);padding:0 6px;position:relative}
.section-title:before{content:"";position:absolute;left:0;right:0;top:5px;border-top:1px solid var(--rule)}

.welcome-text{left:214px;top:401px;width:256px;font-size:6.8px;line-height:11px;color:#555;text-align:center}

/* products */
.product{width:128px;text-align:center}
.product .photo{width:100px;height:96px;margin:0 auto}
.product-name{font-size:7px;font-weight:700;color:#222;margin-top:16px}
.product .blurb{margin-top:9px}
.price-row{display:flex;border-top:1px solid var(--rule);border-bottom:1px solid var(--rule);margin-top:13px;height:27px}
.price-row div{flex:1;font-size:6.5px;color:#555;padding-top:3px;line-height:11px}
.price-row div+div{border-left:1px solid var(--rule)}
.offer b{color:var(--price);font-size:8.5px}
.regular s{color:#999;font-size:8px}
.product .btn{margin-top:13px}
.col-rule{top:540px;width:1px;height:230px;background:var(--rule)}

/* promo tiles */
.promo{top:812px;width:257px;height:106px;color:#fff;overflow:hidden}
.promo-purple{left:74px;background:linear-gradient(90deg,#4a0f5e,#7d2a93 60%,#8a3aa0)}
.promo-dark{left:346px;background:linear-gradient(90deg,#1a1a1a,#3a3a3a 60%,#5a5a5a)}
.promo .art{left:14px;top:8px;width:90px;height:92px}
.promo-script{font-family:"Great Vibes",cursive;font-size:22px;line-height:22px}
.promo-sub{font-size:9px;font-family:"Open Sans",sans-serif}
.promo-save{font-size:11px;line-height:12px}
.promo-save b{font-size:19px}
.promo-cta{right:0;bottom:0;width:54px;height:16px;background:var(--gold);color:#333;font-size:6.5px;font-weight:600;text-align:center;line-height:16px}

/* service strip */
.service-strip{left:0;top:961px;width:677px;height:59px;background:var(--paper)}
.service h4{font-size:7px;font-weight:700;color:#3f5b66}
.service p{font-size:6.5px;color:#555;line-height:9.5px;margin-top:3px}
.strip-rule{top:961px;width:1px;height:59px;background:#e0ddd8}
.card{width:27px;height:17px;border:1px solid #ccc;background:#fff}

/* footer */
.site-footer{left:0;top:1020px;width:677px;height:180px;background:var(--slate);color:#fff}
.newsletter{color:#fff}
.newsletter h4{font-size:7px;font-weight:700}
.newsletter p{font-size:6.5px;color:#e6eef0}
.email-field{left:287px;top:1037px;width:126px;height:16px;border:1px solid #c9d4d8;font-size:6.5px;color:#e6eef0;padding:3px 6px}
.subscribe{left:418px;top:1037px;width:55px;height:16px;background:#e8eef0;color:#3f5b66;font-size:6.5px;font-weight:700;text-align:center;line-height:16px}
.social{top:1037px;width:14px;height:14px;background:#93a6ad}
.footer-col{color:#fff}
.footer-col h5{font-size:7px;font-weight:700;margin-bottom:6px}
.footer-col li{list-style:none;font-size:6.5px;line-height:12.5px;color:#eef3f4}
.footer-col address{font-style:normal;font-size:6.5px;line-height:9.5px;color:#eef3f4}
.copyright{left:74px;top:1165px;width:529px;border-top:1px solid #8fa3aa;text-align:center;font-size:6.5px;color:#eef3f4;padding-top:13px}
</style>
</head>
<body>

<header class="abs site-header">
  <div class="abs brand"><span class="brand-mark"></span>Marrowgate Gemworks</div>
  <div class="abs account-links">My Account | Help<br>Welcome to Marrowgate Gemworks, <span class="accent">Sign In or Register</span></div>
  <div class="abs search">Enter Your Keyword..
    <svg width="10" height="10" viewBox="0 0 10 10"><circle cx="4" cy="4" r="3" fill="none" stroke="#bbb"/><line x1="6.2" y1="6.2" x2="9" y2="9" stroke="#bbb"/></svg>
  </div>
  <nav class="abs main-nav">
    <span style="left:20px">HOME</span><span style="left:84px">SHOP</span><span style="left:146px">OUR STORY</span><span style="left:227px">OUR DIAMONDS</span>
  </nav>
  <div class="abs basket">
    <svg width="9" height="8" viewBox="0 0 9 8"><path d="M0 1h2l1 4h5l1-3H2.5" fill="none" stroke="#fff"/><circle cx="3.5" cy="7" r=".8" fill="#fff"/><circle cx="7" cy="7" r=".8" fill="#fff"/></svg>
    BASKET : 0 ITEM(S) &nbsp;|&nbsp; CHECKOUT
  </div>
</header>

<section>
  <div class="abs category" style="left:74px;top:112px">
    <div class="photo" role="img" aria-label="Model wearing a diamond ring" style="background:linear-gradient(160deg,#c9bfb8,#6b5a52 55%,#2b2626)"></div>
    <div class="cat-title" style="color:var(--orange)">RINGS</div>
    <p class="blurb">This is Draftwork's version of Lorem Ipsum. Proin gravida nibh vel velit auctor aliquet.</p>
    <a class="btn" href="#">SHOP NOW</a>
  </div>
  <div class="abs category" style="left:210px;top:112px">
    <div class="photo" role="img" aria-label="Model wearing a diamond bangle" style="background:linear-gradient(160deg,#cfc7c0,#8c6d5e 50%,#3a2b24)"></div>
    <div class="cat-title" style="color:var(--green)">BANGLES</div>
    <p class="blurb">This is Draftwork's version of Lorem Ipsum. Proin gravida nibh vel velit auctor aliquet.</p>
    <a class="btn" href="#">SHOP NOW</a>
  </div>
  <div class="abs category" style="left:346px;top:112px">
    <div class="photo" role="img" aria-label="Model wearing a pearl necklace" style="background:linear-gradient(160deg,#d9b48c,#b07a55 55%,#5a3a2a)"></div>
    <div class="cat-title" style="color:var(--red)">NECKLACE</div>
    <p class="blurb">This is Draftwork's version of Lorem Ipsum. Proin gravida nibh vel velit auctor aliquet.</p>
    <a class="btn" href="#">SHOP NOW</a>
  </div>
  <div class="abs category" style="left:481px;top:112px">
    <div class="photo" role="img" aria-label="Model wearing diamond ear rings" style="background:linear-gradient(160deg,#f1e6dc,#dfc2a8 55%,#b8957a)"></div>
    <div class="cat-title" style="color:var(--sky)">EAR RINGS</div>
    <p class="blurb">This is Draftwork's version of Lorem Ipsum. Proin gravida nibh vel velit auctor aliquet.</p>
    <a class="btn" href="#">SHOP NOW</a>
  </div>
</section>

<section>
  <h2 class="abs section-title" style="left:74px;top:383px;width:529px;color:var(--teal)"><span>WELCOME TO MARROWGATE GEMWORKS</span></h2>
  <div class="abs photo" role="img" aria-label="Pair of diamond stud ear rings" style="left:74px;top:415px;width:126px;height:68px;background:radial-gradient(ellipse at center,#d8d8d8,#fff 70%)"></div>
  <p class="abs welcome-text">This is Draftwork's version of Lorem Ipsum. Proin gravida nibh vel velit auctor aliquet. Aenean sollicitudin, lorem quis bibendum auctor, nisi elit consequat ipsum, nec sagittis sem nibh id elit. Duis sed odio sit amet nibh vulputate cursus a sit amet mauris. Morbi accumsan ipsum velit.<br><br>Nam nec tellus a odio tincidunt auctor a ornare odio. Sed non mauris vitae erat auctor eu in elit. Class aptent taciti sociosqu ad litora torquent per conubia nostra, per inceptos himenaeos.</p>
  <div class="abs photo" role="img" aria-label="Twisted diamond band ring" style="left:488px;top:402px;width:112px;height:76px;background:radial-gradient(ellipse at center,#cfcfcf,#fff 70%)"></div>
</section>

<section>
  <h2 class="abs section-title" style="left:74px;top:519px;width:258px;color:var(--pink)"><span>NEW ARRIVALS</span></h2>
  <h2 class="abs section-title" style="left:346px;top:519px;width:257px;color:var(--blue)"><span>FEATURED PRODUCTS</span></h2>
  <div class="abs col-rule" style="left:203px"></div>
  <div class="abs col-rule" style="left:339px"></div>
  <div class="abs col-rule" style="left:474px"></div>

  <div class="abs product" style="left:70px;top:546px">
    <div class="photo" role="img" aria-label="Multi-row diamond ring" style="background:radial-gradient(ellipse at center,#bdbdbd,#fff 68%)"></div>
    <div class="product-name">RINGS</div>
    <p class="blurb">This is Draftwork's version of Lorem Proin gravida nibh vel velit.</p>
    <div class="price-row"><div class="offer">Offer Price :<br><b>$800</b></div><div class="regular">Regular Price :<br><s>$1000</s></div></div>
    <a class="btn" href="#">SHOP NOW</a>
  </div>
  <div class="abs product" style="left:206px;top:546px">
    <div class="photo" role="img" aria-label="Diamond eternity band" style="background:radial-gradient(ellipse at center,#cdcdcd,#fff 68%)"></div>
    <div class="product-name">ETERNITY</div>
    <p class="blurb">This is Draftwork's version of Lorem Proin gravida nibh vel velit.</p>
    <div class="price-row"><div class="offer">Offer Price :<br><b>$800</b></div><div class="regular">Regular Price :<br><s>$1000</s></div></div>
    <a class="btn" href="#">SHOP NOW</a>
  </div>
  <div class="abs product" style="left:342px;top:546px">
    <div class="photo" role="img" aria-label="Crown set diamond ring" style="background:radial-gradient(ellipse at center,#c6c6c6,#fff 68%)"></div>
    <div class="product-name">RINGS</div>
    <p class="blurb">This is Draftwork's version of Lorem Proin gravida nibh vel velit.</p>
    <div class="price-row"><div class="offer">Offer Price :<br><b>$800</b></div><div class="regular">Regular Price :<br><s>$1000</s></div></div>
    <a class="btn" href="#">SHOP NOW</a>
  </div>
  <div class="abs product" style="left:477px;top:546px">
    <div class="photo" role="img" aria-label="Diamond eternity band" style="background:radial-gradient(ellipse at center,#cdcdcd,#fff 68%)"></div>
    <div class="product-name">ETERNITY</div>
    <p class="blurb">This is Draftwork's version of Lorem Proin gravida nibh vel velit.</p>
    <div class="price-row"><div class="offer">Offer Price :<br><b>$800</b></div><div class="regular">Regular Price :<br><s>$1000</s></div></div>
    <a class="btn" href="#">SHOP NOW</a>
  </div>
</section>

<section>
  <div class="abs promo promo-purple">
    <div class="abs art" role="img" aria-label="Gold diamond ring" style="background:radial-gradient(ellipse at center,#e0b24a,rgba(224,178,74,0) 70%)"></div>
    <div class="abs" style="left:110px;top:8px;width:140px">
      <div class="promo-script">Diamond</div>
      <div class="promo-script" style="padding-left:46px">Gold</div>
      <div class="promo-sub" style="padding-left:86px;color:#f3c24a">Collections</div>
    </div>
    <div class="abs promo-save" style="left:107px;top:62px">Save Up To<br><b>50%</b> off</div>
    <a class="abs promo-cta" href="#">SHOP NOW</a>
  </div>
  <div class="abs promo promo-dark">
    <div class="abs art" role="img" aria-label="Diamond ring on dark background" style="width:120px;background:radial-gradient(ellipse at center,#9a9a9a,rgba(90,90,90,0) 70%)"></div>
    <div class="abs" style="left:136px;top:8px;width:120px">
      <div class="promo-script">Diamond</div>
      <div class="promo-script" style="padding-left:34px">Rings</div>
      <div class="promo-sub" style="padding-left:70px;color:#f3c24a">Collections</div>
    </div>
    <div class="abs promo-save" style="left:132px;top:67px">Save Up To<br><b>50%</b> off</div>
    <a class="abs promo-cta" href="#">SHOP NOW</a>
  </div>
</section>

<section class="abs service-strip"></section>
<div class="abs strip-rule" style="left:245px"></div>
<div class="abs strip-rule" style="left:432px"></div>
<div class="abs service" style="left:74px;top:972px;display:flex;gap:8px">
  <svg width="22" height="28" viewBox="0 0 22 28"><rect x="1" y="1" width="20" height="22" rx="3" fill="var(--slate)"/><rect x="4" y="4" width="14" height="8" fill="var(--paper)"/><rect x="3" y="23" width="4" height="4" fill="var(--slate)"/><rect x="15" y="23" width="4" height="4" fill="var(--slate)"/></svg>
  <div><h4>FREE DELIVERY</h4><p>On All orders over $25 Everyday!</p></div>
</div>
<div class="abs service" style="left:259px;top:972px;display:flex;gap:8px">
  <svg width="24" height="28" viewBox="0 0 24 28"><circle cx="12" cy="8" r="7" fill="var(--slate)"/><path d="M1 28c0-8 5-12 11-12s11 4 11 12z" fill="var(--slate)"/></svg>
  <div><h4>ONLINE SUPPORT</h4><p>Email and Live Chat support is available<br>Help link is at the top of the page.</p></div>
</div>
<div class="abs service" style="left:444px;top:970px"><h4>PAYMENT METHOD</h4></div>
<div class="abs card" style="left:444px;top:990px;background:#e9eef5"></div>
<div class="abs card" style="left:475px;top:990px;background:#f7efe6"></div>
<div class="abs card" style="left:506px;top:990px;background:#4a8fc7;border-color:#4a8fc7"></div>
<div class="abs card" style="left:537px;top:990px;background:#d94a2a;border-color:#d94a2a"></div>
<div class="abs card" style="left:568px;top:990px;background:#27468f;border-color:#27468f"></div>

<footer class="abs site-footer"></footer>
<div class="abs newsletter" style="left:74px;top:1034px;display:flex;gap:7px">
  <svg width="18" height="16" viewBox="0 0 18 16"><path d="M0 7L18 0 14 16 8 11z" fill="#dfe7ea"/></svg>
  <div><h4>SUBSCRIBE OUR NEWSLETTER!</h4><p>Signup to get exclusive offers from your favorite brands.</p></div>
</div>
<div class="abs email-field">Enter Your Email Address...</div>
<div class="abs subscribe">SUBSCRIBE</div>
<div class="abs social" style="left:512px"></div>
<div class="abs social" style="left:531px"></div>
<div class="abs social" style="left:550px"></div>
<div class="abs social" style="left:569px"></div>
<div class="abs social" style="left:588px"></div>

<div class="abs footer-col" style="left:74px;top:1079px"><h5>OUR PRODUCT RANGE</h5><ul><li>Rings</li><li>Bangles</li><li>Necklace</li><li>Ear Rings</li><li>Bracelets</li></ul></div>
<div class="abs footer-col" style="left:211px;top:1079px"><h5>HELP</h5><ul><li>Contact Us</li><li>About Us</li><li>Shipping</li><li>Help / FAQs</li></ul></div>
<div class="abs footer-col" style="left:313px;top:1079px"><h5>COMPANY INFO</h5><ul><li>Careers</li><li>Terms of Use</li><li>Privacy Policy</li></ul></div>
<div class="abs footer-col" style="left:421px;top:1079px"><h5>CART</h5><ul><li>View Cart</li><li>My Account</li><li>Order Status</li><li>Login</li></ul></div>
<div class="abs footer-col" style="left:519px;top:1079px"><h5>CONTACT US</h5><address>27 Larkspur Road,<br>#03-12 Fernhill Arcade,<br>Singapore 580412<br><br>Tel: +65 9000 1234</address></div>

<div class="abs copyright">Copyright © 2013 Marrowgate Gemworks. All Rights Reserved.</div>

</body>
</html>
```